brochure for high-end senior living company

We need a new brochure that we can pass out to doctors and social workers so they would choose us over the competition.
brightmeadowhaven.example is our website that shows our colors and themes

we stand out over our competition due to our high quality of staff and our staff to resident ratio.
We are not afraid of difficult and complex care situations. Instead, we thrive on coordinating complexity.

We do all of this in a lovely setting that is luxurious and feels like home.

Target Market(s)

The families who make the decision are 60-70 years old. They are not not "rich" but they have saved well and usually have more than 1 million in assets.

Industry/Entity Type

Senior Living, Memory Care

Font styles to use
Serif

Colors
00AB8E
00BBA5
67D7C9
C6EFE9
E9F9F6
FFC000
F8CF3A
FAE287
FDF2CF
FEFAEE

Requirements
Must have
• When compromise is not an option...
Nice to have
• A difficult balance of beautiful and activities (happy people), but also communicating that we handle difficult and complex care.

```html
<!DOCTYPE html>
<html lang="en">
<head>
<meta charset="utf-8">
<title>Bright Meadow Haven – Reasons to Choose Us</title>
<link rel="stylesheet" href="https://fonts.googleapis.com/css2?family=Lora:ital,wght@0,400;0,600;0,700;1,500&display=swap">
<style>
  :root {
    --ink-teal: #0a3f3a;
    --panel-teal: #064a43;
    --teal: #00ab8e;
    --teal-soft: #67d7c9;
    --gold: #c99700;
    --gold-bright: #f8cf3a;
    --gold-rule: #ffc000;
    --white: #ffffff;
    --paper: #ffffff;
  }
  * { box-sizing: border-box; margin: 0; padding: 0; }
  html, body { width: 848px; height: 1200px; overflow: hidden; background: var(--paper); }
  body { font-family: "Lora", Georgia, serif; position: relative; }

  .brand {
    position: absolute; top: 140px; left: 0; width: 848px; text-align: center;
    color: var(--ink-teal);
  }
  .brand-name {
    font-size: 46px; font-weight: 600; letter-spacing: 0.5px; line-height: 1;
  }
  .brand-tagline {
    margin-top: 16px; font-size: 24px; font-weight: 400; line-height: 1;
  }

  .promise {
    position: absolute; top: 268px; left: 0; width: 848px; text-align: center;
    color: var(--teal); font-size: 21px; font-style: italic; font-weight: 500; line-height: 1;
  }

  .section-title {
    position: absolute; top: 318px; left: 0; width: 848px; text-align: center;
    color: var(--gold); font-size: 40px; font-weight: 700; line-height: 1;
  }

  .reasons {
    position: absolute; left: 44px; top: 403px; width: 759px; height: 471px;
    background: var(--panel-teal); border: 2px solid var(--gold-rule);
  }
  .reason {
    position: absolute; width: 320px; text-align: center; color: var(--white);
    font-size: 21px; font-weight: 600; line-height: 27px;
  }
  .reason svg { display: block; margin: 0 auto; fill: var(--gold-bright); }
  .reason-private { left: 18px; top: 46px; }
  .reason-private p { margin-top: 36px; }
  .reason-meals { left: 412px; top: 44px; }
  .reason-meals p { margin-top: 20px; }
  .reason-ratio { left: 18px; top: 266px; }
  .reason-ratio p { margin-top: 24px; }
  .reason-staff { left: 412px; top: 266px; }
  .reason-staff p { margin-top: 30px; }

  .contact {
    position: absolute; top: 1010px; left: 0; width: 848px; text-align: center;
    color: var(--ink-teal); font-size: 30px; font-weight: 700; line-height: 40px;
  }
  .contact-phone { color: var(--gold); }
</style>
</head>
<body>
  <header class="brand">
    <div class="brand-name">Bright Meadow Haven</div>
    <div class="brand-tagline">Residential Assisted Living</div>
  </header>

  <p class="promise">When compromise is not an option...</p>

  <h1 class="section-title">Reasons to Choose Us</h1>

  <section class="reasons">
    <div class="reason reason-private">
      <svg width="58" height="42" viewBox="0 0 58 42" aria-hidden="true">
        <rect x="0" y="0" width="5" height="42"/>
        <rect x="53" y="16" width="5" height="26"/>
        <rect x="0" y="28" width="58" height="6"/>
        <circle cx="14" cy="15" r="6"/>
        <rect x="23" y="10" width="32" height="14" rx="3"/>
        <rect x="7" y="21" width="16" height="5" rx="2"/>
      </svg>
      <p>Private Rooms<br>and Bathrooms</p>
    </div>

    <div class="reason reason-meals">
      <svg width="60" height="52" viewBox="0 0 60 52" aria-hidden="true">
        <rect x="2" y="0" width="2.5" height="16"/>
        <rect x="6.5" y="0" width="2.5" height="16"/>
        <rect x="11" y="0" width="2.5" height="16"/>
        <rect x="2" y="14" width="11.5" height="5" rx="2"/>
        <rect x="5.5" y="18" width="4.5" height="34" rx="2"/>
        <circle cx="30" cy="26" r="17"/>
        <circle cx="30" cy="26" r="12" fill="var(--panel-teal)"/>
        <circle cx="30" cy="26" r="9.5"/>
        <path d="M52 0 C58 8 58 22 54 26 L54 52 L50 52 L50 0 Z"/>
      </svg>
      <p>Delicious and Healthy<br>Home Cooked Meals</p>
    </div>

    <div class="reason reason-ratio">
      <svg width="58" height="56" viewBox="0 0 58 56" aria-hidden="true">
        <path d="M29 26 L18 15 A6.5 6.5 0 0 1 29 6 A6.5 6.5 0 0 1 40 15 Z"/>
        <rect x="0" y="38" width="9" height="16"/>
        <path d="M11 38 C18 33 25 33 32 37 L40 37 C44 37 44 43 40 43 L28 43 L40 44 L52 35 C56 32 60 37 56 40 L42 52 C40 54 38 54 35 54 L11 54 Z"/>
      </svg>
      <p>Highest Caregiver to<br>Resident Ratio in the<br>Industry</p>
    </div>

    <div class="reason reason-staff">
      <svg width="58" height="58" viewBox="0 0 58 58" aria-hidden="true">
        <circle cx="29" cy="29" r="29"/>
        <circle cx="29" cy="29" r="22" fill="var(--panel-teal)"/>
        <circle cx="29" cy="29" r="19"/>
        <path d="M20 22 L29 31 L38 22" fill="none" stroke="var(--panel-teal)" stroke-width="3.5" stroke-linecap="round" stroke-linejoin="round"/>
      </svg>
      <p>24/7 Well-Trained<br>Caregivers on Site</p>
    </div>
  </section>

  <footer class="contact">
    <p>Contact our Maplewood Assisted Living<br>Home Today At<br><span class="contact-phone">(555) 014-2290!</span></p>
  </footer>
</body>
</html>
```